Visitenkarten für Psychotherapeutin
Zielgruppe
Ich war Psychologin und Coachin und bin jetzt eine approbierte Psychotherapeutin.
Aufgabenstellung
Es gibt ein Layout, an das sich angelehnt werden soll.
Die Farb- und Schriftwelt liegt vor, jedoch soll aus dem türkies ein warmer Pink-Rot-Ton werden.
Die Visitenkarte soll für die neu eröffnete Privatpraxis verwendet werden. Im Logo soll die Berufsbezeichnung Psychologische Psychotherapeutin (mit) Schwerpunkt Systemische Therapie stehen.
Neben den Kontaktdaten folgender Text:
Privatpraxis für Psychologische Psychotherapie, Schwerpunkt Systemische Therapie
Für Privatversicherte und Selbstzahlende
Termin nach Vereinbarung
Die Zeile mit der Sprechstunde soll weg.

```html
<!DOCTYPE html>
<html lang="de">
<head>
<meta charset="utf-8">
<title>Visitenkarte Hanna Morbach</title>
<link href="https://fonts.googleapis.com/css2?family=Montserrat:wght@400;500;600;700&display=swap" rel="stylesheet">
<style>
  :root {
    --bg: #f1f1f1;
    --paper: #ffffff;
    --berry: #5f0632;
    --berry-soft: #6b0d3b;
    --ink: #2b2b2b;
    --white: #ffffff;
  }
  * { box-sizing: border-box; margin: 0; padding: 0; }
  html, body { width: 1200px; height: 900px; overflow: hidden; }
  body {
    background: var(--bg);
    font-family: "Montserrat", sans-serif;
    position: relative;
  }
  .card {
    position: absolute;
    width: 520px;
    height: 336px;
    box-shadow: 0 6px 18px rgba(0,0,0,0.12);
    overflow: hidden;
  }
  /* Front */
  .card-front { left: 70px; top: 110px; background: var(--paper); }
  .front-identity { position: absolute; left: 40px; top: 92px; }
  .front-name {
    color: var(--berry);
    font-weight: 700;
    font-size: 19px;
    letter-spacing: 0.5px;
  }
  .front-title {
    color: var(--ink);
    font-size: 12.5px;
    line-height: 1.45;
    margin-top: 4px;
  }
  .appointment-stamp {
    position: absolute;
    right: 44px; top: 34px;
    width: 96px; height: 96px;
    border: 1.5px solid var(--berry);
    border-radius: 50%;
    display: flex; align-items: center; justify-content: center;
    text-align: center;
    color: var(--berry);
    font-size: 10.5px;
    font-weight: 500;
    line-height: 1.3;
  }
  .contact-row {
    position: absolute;
    left: 40px; right: 36px; bottom: 66px;
    display: flex; justify-content: space-between; align-items: flex-end;
    font-size: 12px;
    color: var(--ink);
    line-height: 1.55;
  }
  .contact-web { color: var(--berry); }
  .front-band {
    position: absolute;
    left: 0; right: 0; bottom: 0;
    height: 46px;
    background: var(--berry);
    color: var(--white);
    display: flex; align-items: center; justify-content: center;
    font-size: 11.5px;
    font-weight: 600;
    letter-spacing: 1.6px;
  }
  /* Back */
  .card-back { left: 610px; top: 454px; background: var(--berry); }
  .back-decor { position: absolute; inset: 0; }
  .back-logo { position: absolute; left: 42px; bottom: 46px; color: var(--white); }
  .back-name { font-size: 34px; font-weight: 500; letter-spacing: 0.5px; }
  .back-title {
    margin-top: 8px;
    font-size: 8.5px;
    font-weight: 600;
    letter-spacing: 1px;
    line-height: 1.5;
  }
  .back-claim {
    position: absolute;
    right: 40px; top: 118px;
    color: var(--white);
    font-size: 13px;
    line-height: 1.5;
    text-align: right;
  }
</style>
</head>
<body>

<section class="card card-front">
  <div class="front-identity">
    <div class="front-name">HANNA MORBACH</div>
    <div class="front-title">Psychologische Psychotherapeutin<br>mit Schwerpunkt Systemische Therapie</div>
  </div>
  <div class="appointment-stamp">Termin<br>nach<br>Vereinbarung</div>
  <div class="contact-row">
    <div class="contact-address">Lindenhofweg 12<br>85640 Musterkirchen</div>
    <div class="contact-reach">+49 170 2048391<br>kontakt@hmorbachtu.de</div>
    <div class="contact-web">www.hmorbachtu.de</div>
  </div>
  <div class="front-band">FÜR PRIVATVERSICHERTE UND SELBSTZAHLENDE</div>
</section>

<section class="card card-back">
  <svg class="back-decor" width="520" height="336" role="img" aria-label="Große, dezente Schriftzug-Dekoration des Namens im Hintergrund">
    <defs>
      <radialGradient id="decorGlow" cx="60%" cy="40%" r="60%">
        <stop offset="0" stop-color="#55042c"/>
        <stop offset="1" stop-color="#5f0632" stop-opacity="0"/>
      </radialGradient>
    </defs>
    <rect width="520" height="336" fill="url(#decorGlow)"/>
  </svg>
  <div class="back-claim">Vertrauen.<br>Menschlichkeit.<br>Kompetenz.</div>
  <div class="back-logo">
    <div class="back-name">Hanna Morbach</div>
    <div class="back-title">PSYCHOLOGISCHE PSYCHOTHERAPEUTIN<br>MIT SCHWERPUNKT SYSTEMISCHE THERAPIE</div>
  </div>
</section>

</body>
</html>
```